Business card design for Birch Engineering Torvant

We need a new business card design along with all the necessary to place an order. The company is Birch Engineering Torvant and we recently updated our logo.

```html
<!DOCTYPE html>
<html lang="en">
<head>
<meta charset="utf-8">
<title>Birch Engineering Torvant – Business Card</title>
<link rel="stylesheet" href="https://fonts.googleapis.com/css2?family=Kanit:wght@400;600&display=swap">
<style>
  :root {
    --backdrop: #2e2e2e;
    --card: #1d1d1d;
    --accent: #e4c02a;
    --text: #f1f1f1;
    --brand-grey: #9c9c9c;
    --shade-light: #3a3a3a;
    --shade-dark: #0c0c0c;
  }
  * { margin: 0; padding: 0; box-sizing: border-box; }
  html, body { width: 1200px; height: 1059px; overflow: hidden; }
  body {
    background: var(--backdrop);
    font-family: "Kanit", sans-serif;
    position: relative;
  }
  .card {
    position: absolute;
    background: var(--card);
    border-radius: 24px;
    overflow: hidden;
  }
  .card--front { left: 256px; top: 100px; width: 688px; height: 393px; }
  .card--back  { left: 253px; top: 535px; width: 694px; height: 397px; }

  .brand {
    position: absolute;
    display: flex;
    align-items: center;
    gap: 12px;
  }
  .brand__mark {
    width: 16px; height: 16px;
    background: var(--accent);
    flex: none;
  }
  .brand__name {
    color: var(--brand-grey);
    font-weight: 600;
    font-size: 27px;
    line-height: 1.1;
    letter-spacing: 0.5px;
  }
  .card--front .brand { left: 34px; top: 162px; }
  .card--back .brand { right: 34px; top: 298px; flex-direction: row-reverse; text-align: right; }

  .divider {
    position: absolute;
    left: 340px; top: 82px;
    width: 2px; height: 230px;
    background: var(--accent);
  }
  .details {
    position: absolute;
    left: 357px; top: 76px;
    color: var(--text);
  }
  .details__name {
    color: var(--accent);
    font-weight: 600;
    font-size: 32px;
    line-height: 1;
    letter-spacing: 0.3px;
  }
  .details__role { font-size: 17px; margin-top: 10px; line-height: 1.2; }
  .details__company { font-size: 17.5px; margin-top: 26px; line-height: 1.6; }
  .contact { list-style: none; margin-top: 16px; }
  .contact__item {
    display: flex; align-items: center; gap: 9px;
    font-size: 17.5px; line-height: 27px;
  }
  .contact__icon { width: 15px; height: 15px; flex: none; fill: var(--accent); }

  .back-visual {
    position: absolute;
    left: 0; top: 0; width: 460px; height: 397px;
    background: radial-gradient(ellipse at 55% 35%, var(--shade-light) 0%, #1f1f1f 45%, var(--shade-dark) 100%);
    opacity: 0.85;
  }
</style>
</head>
<body>
  <section class="card card--front">
    <div class="brand">
      <span class="brand__mark"></span>
      <span class="brand__name">Birch Engineering<br>Torvant</span>
    </div>
    <div class="divider"></div>
    <div class="details">
      <h1 class="details__name">DANIEL HALE</h1>
      <p class="details__role">Managing Director</p>
      <p class="details__company">Birch Engineering Torvant<br>24b Fenwick Road, Corby NN17 4RT</p>
      <ul class="contact">
        <li class="contact__item">
          <svg class="contact__icon" viewBox="0 0 16 16"><path d="M1 6c0-2 3-3.5 7-3.5S15 4 15 6v1.5h-3.5V6H4.5v1.5H1z M3 9l2-2h6l2 2v5H3z"/></svg>
          01536 482907
        </li>
        <li class="contact__item">
          <svg class="contact__icon" viewBox="0 0 16 16"><path d="M1 3h14v1.5L8 9 1 4.5z M1 6.5 8 11l7-4.5V13H1z"/></svg>
          sales@birchengineering.co.uk
        </li>
        <li class="contact__item">
          <svg class="contact__icon" viewBox="0 0 16 16"><circle cx="8" cy="8" r="7"/></svg>
          www.birchengineering.co.uk
        </li>
      </ul>
    </div>
  </section>

  <section class="card card--back">
    <div class="back-visual" role="img" aria-label="Large brand mark decoration in grey and black gradients"></div>
    <div class="brand">
      <span class="brand__mark"></span>
      <span class="brand__name">Birch Engineering<br>Torvant</span>
    </div>
  </section>
</body>
</html>
```